2 Flow Charts showing Fair Trade vs Market Trade****See new image*****

I am starting a coffee roasting company where I warehouse coffee for farmers I met in Nicaragua as a Unity Service Brigade Volunteer.

I need one flow chart to show the normal path of coffee, from the producer to the exporter, to the importer, to the roaster, and ultimately to the consumer, each of which taking a little along the way, leaving the farmer less.

Then another flow chart showing a close relationship between my company (Lark Hollow Coffee) and the producer, with out the exporter/importer, and more money going to the farmer.

I have included my attempt at the flow charts, which look clunky and are in super low res.

You can see how I want to use the flow charts in the following website:

larkhollowbeanworks.com

****** Just reduced the verbiage on the Flow Charts****************
***************See new image*******************************

Target Market(s)

Coffee consumers interested in fair trade.

Industry/Entity Type

It Company

Font styles to use
Sans Serif

Requirements
Must have
• Originally thinking black and white, but am open to color.
Nice to have
• Would like to see a design in both color and monochrome. I am having a difficult time determining which would look better on the site.

```html
<!DOCTYPE html>
<html lang="en">
<head>
<meta charset="utf-8">
<title>The Lark Hollow Model</title>
<link rel="stylesheet" href="https://fonts.googleapis.com/css2?family=Jost:wght@400;500;600;700;800&display=swap">
<style>
  :root{
    --paper:#ffffff;
    --rule:#000000;
  }
  html,body{margin:0;padding:0;overflow:hidden;background:var(--paper);}
  .canvas{position:relative;width:1200px;height:1000px;overflow:hidden;background:var(--paper);font-family:"Jost",sans-serif;}
  .model{position:absolute;left:0;width:1200px;height:490px;display:block;}
  .model--color{top:0;
    --ink:#3a87c8;--hot:#f04a23;--trail:#f6c3b3;--bean:#7b4a33;--figure:#9cc3e4;--brand:#f04a23;--node-fill:#f04a23;}
  .model--mono{top:498px;
    --ink:#111111;--hot:#111111;--trail:#111111;--bean:#111111;--figure:#8a8a8a;--brand:#111111;--node-fill:#111111;}
  .divider{position:absolute;left:38px;top:493px;width:1125px;height:9px;background:var(--rule);}

  .model text{font-family:"Jost",sans-serif;}
  .title{fill:var(--ink);font-size:41px;font-weight:800;}
  .tagline{fill:var(--ink);font-size:16.5px;font-weight:600;}
  .bracket{fill:none;stroke:var(--hot);stroke-width:2;}
  .tab{fill:var(--ink);}
  .tab-text{fill:#ffffff;font-size:15px;font-weight:700;letter-spacing:0.3px;}
  .flow{fill:none;stroke:var(--ink);stroke-width:2;}
  .trail{fill:none;stroke:var(--trail);stroke-width:2;}
  .trail-label{fill:var(--trail);font-size:10.5px;font-weight:700;}
  .icon{fill:none;stroke:var(--ink);stroke-width:2;stroke-linejoin:round;}
  .role-label{fill:var(--ink);font-size:7.5px;font-weight:700;}
  .node{fill:#ffffff;stroke:var(--hot);stroke-width:2;}
  .node--filled{fill:var(--node-fill);stroke:var(--ink);}
  .node-num{fill:var(--ink);font-size:8px;font-weight:700;}
  .node-num--light{fill:#ffffff;}
  .bean{fill:var(--bean);}
  .figure{fill:var(--figure);}
  .caption{fill:var(--ink);font-size:12px;font-weight:500;}
  .caption--wide{font-size:12.5px;}
  .your-coffee{fill:var(--ink);font-size:11px;font-weight:800;}
  .note{fill:var(--ink);font-size:12px;font-weight:400;}
  .brand-label{fill:var(--ink);font-size:11px;font-weight:700;}
  .brand-mark{fill:var(--brand);}
  .money{fill:var(--ink);font-size:22px;font-weight:800;}
  .hero-coffee{fill:var(--brand);font-size:18px;font-weight:800;}
  .hero-sub{fill:var(--brand);font-size:12.5px;font-weight:400;letter-spacing:0.4px;}
  .arrowhead{fill:var(--ink);}
  .arrowhead--trail{fill:var(--trail);}
  .big-node{fill:#ffffff;stroke:var(--hot);stroke-width:2;}
  .big-num{fill:var(--ink);font-size:10px;font-weight:700;}
  .big-num--light{fill:#ffffff;}
</style>
</head>
<body>
<main class="canvas">

  <svg class="model model--color" viewBox="0 0 1200 490" aria-label="The Lark Hollow model, colour">
    <defs>
      <marker id="arrow-color" viewBox="0 0 10 10" refX="8" refY="5" markerWidth="7" markerHeight="7" orient="auto"><path class="arrowhead" d="M0 0 L10 5 L0 10 z"/></marker>
      <marker id="trail-color" viewBox="0 0 10 10" refX="8" refY="5" markerWidth="5" markerHeight="5" orient="auto"><path class="arrowhead--trail" d="M0 1 L10 5 L0 9 z"/></marker>
    </defs>

    <text class="title" x="600" y="86" text-anchor="middle" textLength="474" lengthAdjust="spacingAndGlyphs">THE LARK HOLLOW MODEL</text>
    <path class="bracket" d="M264 99 H259 V127 H264"/>
    <path class="bracket" d="M936 99 H941 V127 H936"/>
    <text class="tagline" x="600" y="119" text-anchor="middle">We do things differently. We do away with the middlemen and give more to the farmers.</text>

    <rect class="tab" x="257" y="147" width="185" height="25"/>
    <text class="tab-text" x="349.5" y="165" text-anchor="middle">TRADITIONAL TRADE</text>
    <rect class="tab" x="757" y="147" width="185" height="25"/>
    <text class="tab-text" x="849.5" y="165" text-anchor="middle">LARK HOLLOW TRADE</text>

    <g class="traditional">
      <rect class="figure" x="176" y="187" width="52" height="42" rx="6" role="img" aria-label="Coffee tree and farmer illustration"/>
      <text class="role-label" x="203" y="237" text-anchor="middle">PRODUCER</text>

      <path class="flow" d="M203 245 V280 H261"/>
      <path class="flow" d="M267 286 V316 H321"/>
      <path class="flow" d="M327 322 V355 H386"/>
      <path class="flow" d="M392 361 V392 H437"/>

      <ellipse class="bean" cx="233" cy="280" rx="4" ry="2.6" transform="rotate(-40 233 280)"/>
      <ellipse class="bean" cx="295" cy="316" rx="4" ry="2.6" transform="rotate(-40 295 316)"/>
      <ellipse class="bean" cx="358" cy="355" rx="4" ry="2.6" transform="rotate(-40 358 355)"/>
      <ellipse class="bean" cx="418" cy="392" rx="4" ry="2.6" transform="rotate(-40 418 392)"/>

      <circle class="node node--filled" cx="203" cy="245" r="6"/><text class="node-num node-num--light" x="203" y="248" text-anchor="middle">1</text>
      <circle class="node" cx="267" cy="280" r="6"/><text class="node-num" x="267" y="283" text-anchor="middle">2</text>
      <circle class="node" cx="327" cy="316" r="6"/><text class="node-num" x="327" y="319" text-anchor="middle">3</text>
      <circle class="node" cx="392" cy="355" r="6"/><text class="node-num" x="392" y="358" text-anchor="middle">4</text>
      <circle class="node node--filled" cx="443" cy="392" r="6"/><text class="node-num node-num--light" x="443" y="395" text-anchor="middle">5</text>

      <path class="icon" d="M252 257 V241 A17 15 0 0 1 286 241 V257 Z M258 257 V245 H280 V257 M258 249 H280 M258 253 H280 M286 243 L291 246 V257 H286"/>
      <text class="role-label" x="268" y="267" text-anchor="middle">EXPORTER</text>
      <path class="icon" d="M316 294 V278 L329 266 L342 278 V294 Z M323 294 V283 H335 V294"/>
      <text class="role-label" x="329" y="304" text-anchor="middle">IMPORTER</text>
      <path class="icon" d="M375 321 L392 305 L409 321 M380 317 V334 H404 V317 M387 334 V325 H397 V334"/>
      <text class="role-label" x="392" y="343" text-anchor="middle">COFFEE ROASTER</text>
      <path class="icon" d="M462 378 H492 V388 A10 10 0 0 1 482 398 H472 A10 10 0 0 1 462 388 Z M492 381 H496 A5 5 0 0 1 496 391 H491"/>
      <ellipse class="bean" cx="477" cy="387" rx="5" ry="3.6" transform="rotate(-40 477 387)"/>
      <path class="icon" d="M474 371 Q471 367 474 364 M479 371 Q476 367 479 364" stroke-width="1.2"/>
      <text class="your-coffee" x="466" y="411" text-anchor="middle">YOUR COFFEE</text>

      <path class="trail" d="M271 228 V204 H262"/>
      <text class="trail-label" x="256" y="207.5" text-anchor="middle">$</text>
      <path class="trail" d="M250 204 H236" marker-end="url(#trail-color)"/>

      <path class="trail" d="M330 264 V244 H322"/>
      <text class="trail-label" x="313" y="247.5" text-anchor="middle">$$</text>
      <path class="trail" d="M304 244 H294" marker-end="url(#trail-color)"/>

      <path class="trail" d="M394 303 V281 H384"/>
      <text class="trail-label" x="371" y="284.5" text-anchor="middle">$$$</text>
      <path class="trail" d="M358 281 H345" marker-end="url(#trail-color)"/>

      <path class="trail" d="M480 360 V322 H462"/>
      <text class="trail-label" x="446" y="325.5" text-anchor="middle">$$$$</text>
      <path class="trail" d="M429 322 H412" marker-end="url(#trail-color)"/>

      <text class="caption" x="349" y="440" text-anchor="middle">Traditionally, farmers sell their coffee for <tspan font-weight="700">1$ to $1.85 a pound</tspan></text>
    </g>

    <g class="direct">
      <rect class="figure" x="680" y="196" width="56" height="43" rx="6" role="img" aria-label="Coffee tree and farmer illustration"/>
      <text class="brand-label" x="713" y="252" text-anchor="middle">PRODUCER</text>
      <rect class="brand-mark" x="967" y="196" width="40" height="40"/>
      <text class="brand-label" x="987" y="252" text-anchor="middle">LARK HOLLOW</text>

      <text class="note" x="850" y="216" text-anchor="middle">We directly</text>
      <text class="note" x="850" y="231" text-anchor="middle">import &amp; roast</text>
      <text class="note" x="850" y="246" text-anchor="middle">the coffee</text>

      <path class="flow" d="M721 266 H979"/>
      <path class="flow" d="M845 363 L723 274" marker-end="url(#arrow-color)"/>
      <path class="flow" d="M859 363 L979 274" marker-end="url(#arrow-color)"/>

      <circle class="big-node" cx="713" cy="266" r="8"/><text class="big-num" x="713" y="270" text-anchor="middle">1</text>
      <circle class="big-node" cx="987" cy="266" r="8"/><text class="big-num" x="987" y="270" text-anchor="middle">2</text>
      <circle class="big-node" cx="850" cy="266" r="13"/>
      <ellipse class="bean" cx="850" cy="266" rx="6" ry="8.5" transform="rotate(25 850 266)"/>

      <text class="money" x="788" y="333" text-anchor="middle" transform="rotate(-35 788 326)">$$</text>
      <text class="money" x="920" y="333" text-anchor="middle" transform="rotate(35 920 326)">$$</text>

      <path class="icon" d="M831 332 H868 V345 A12 12 0 0 1 856 357 H843 A12 12 0 0 1 831 345 Z M868 336 H873 A6 6 0 0 1 873 348 H866"/>
      <rect class="brand-mark" x="843" y="337" width="13" height="13"/>
      <path class="icon" d="M845 325 Q842 320 845 316 M851 325 Q848 320 851 316" stroke-width="1.3"/>
      <circle class="node node--filled" cx="852" cy="370" r="8"/><text class="big-num big-num--light" x="852" y="374" text-anchor="middle">3</text>

      <text class="hero-coffee" x="853" y="398" text-anchor="middle">YOUR COFFEE</text>
      <text class="hero-sub" x="853" y="412" text-anchor="middle">FROM LARK HOLLOW</text>

      <text class="caption caption--wide" x="850" y="436" text-anchor="middle">We share revenues, guaranteeing our farmers <tspan font-weight="700">$3.25 a pound</tspan></text>
    </g>
  </svg>

  <div class="divider"></div>

  <svg class="model model--mono" viewBox="0 0 1200 490" aria-label="The Lark Hollow model, monochrome">
    <defs>
      <marker id="arrow-mono" viewBox="0 0 10 10" refX="8" refY="5" markerWidth="7" markerHeight="7" orient="auto"><path class="arrowhead" d="M0 0 L10 5 L0 10 z"/></marker>
      <marker id="trail-mono" viewBox="0 0 10 10" refX="8" refY="5" markerWidth="5" markerHeight="5" orient="auto"><path class="arrowhead--trail" d="M0 1 L10 5 L0 9 z"/></marker>
    </defs>

    <text class="title" x="600" y="86" text-anchor="middle" textLength="474" lengthAdjust="spacingAndGlyphs">THE LARK HOLLOW MODEL</text>
    <path class="bracket" d="M264 99 H259 V127 H264"/>
    <path class="bracket" d="M936 99 H941 V127 H936"/>
    <text class="tagline" x="600" y="119" text-anchor="middle">We do things differently. We do away with the middlemen and give more to the farmers.</text>

    <rect class="tab" x="257" y="147" width="185" height="25"/>
    <text class="tab-text" x="349.5" y="165" text-anchor="middle">TRADITIONAL TRADE</text>
    <rect class="tab" x="757" y="147" width="185" height="25"/>
    <text class="tab-text" x="849.5" y="165" text-anchor="middle">LARK HOLLOW TRADE</text>

    <g class="traditional">
      <rect class="figure" x="176" y="187" width="52" height="42" rx="6" role="img" aria-label="Coffee tree and farmer illustration"/>
      <text class="role-label" x="203" y="237" text-anchor="middle">PRODUCER</text>

      <path class="flow" d="M203 245 V280 H261"/>
      <path class="flow" d="M267 286 V316 H321"/>
      <path class="flow" d="M327 322 V355 H386"/>
      <path class="flow" d="M392 361 V392 H437"/>

      <ellipse class="bean" cx="233" cy="280" rx="4" ry="2.6" transform="rotate(-40 233 280)"/>
      <ellipse class="bean" cx="295" cy="316" rx="4" ry="2.6" transform="rotate(-40 295 316)"/>
      <ellipse class="bean" cx="358" cy="355" rx="4" ry="2.6" transform="rotate(-40 358 355)"/>
      <ellipse class="bean" cx="418" cy="392" rx="4" ry="2.6" transform="rotate(-40 418 392)"/>

      <circle class="node node--filled" cx="203" cy="245" r="6"/><text class="node-num node-num--light" x="203" y="248" text-anchor="middle">1</text>
      <circle class="node" cx="267" cy="280" r="6"/><text class="node-num" x="267" y="283" text-anchor="middle">2</text>
      <circle class="node" cx="327" cy="316" r="6"/><text class="node-num" x="327" y="319" text-anchor="middle">3</text>
      <circle class="node" cx="392" cy="355" r="6"/><text class="node-num" x="392" y="358" text-anchor="middle">4</text>
      <circle class="node node--filled" cx="443" cy="392" r="6"/><text class="node-num node-num--light" x="443" y="395" text-anchor="middle">5</text>

      <path class="icon" d="M252 257 V241 A17 15 0 0 1 286 241 V257 Z M258 257 V245 H280 V257 M258 249 H280 M258 253 H280 M286 243 L291 246 V257 H286"/>
      <text class="role-label" x="268" y="267" text-anchor="middle">EXPORTER</text>
      <path class="icon" d="M316 294 V278 L329 266 L342 278 V294 Z M323 294 V283 H335 V294"/>
      <text class="role-label" x="329" y="304" text-anchor="middle">IMPORTER</text>
      <path class="icon" d="M375 321 L392 305 L409 321 M380 317 V334 H404 V317 M387 334 V325 H397 V334"/>
      <text class="role-label" x="392" y="343" text-anchor="middle">COFFEE ROASTER</text>
      <path class="icon" d="M462 378 H492 V388 A10 10 0 0 1 482 398 H472 A10 10 0 0 1 462 388 Z M492 381 H496 A5 5 0 0 1 496 391 H491"/>
      <ellipse class="bean" cx="477" cy="387" rx="5" ry="3.6" transform="rotate(-40 477 387)"/>
      <path class="icon" d="M474 371 Q471 367 474 364 M479 371 Q476 367 479 364" stroke-width="1.2"/>
      <text class="your-coffee" x="466" y="411" text-anchor="middle">YOUR COFFEE</text>

      <path class="trail" d="M271 228 V204 H262"/>
      <text class="trail-label" x="256" y="207.5" text-anchor="middle">$</text>
      <path class="trail" d="M250 204 H236" marker-end="url(#trail-mono)"/>

      <path class="trail" d="M330 264 V244 H322"/>
      <text class="trail-label" x="313" y="247.5" text-anchor="middle">$$</text>
      <path class="trail" d="M304 244 H294" marker-end="url(#trail-mono)"/>

      <path class="trail" d="M394 303 V281 H384"/>
      <text class="trail-label" x="371" y="284.5" text-anchor="middle">$$$</text>
      <path class="trail" d="M358 281 H345" marker-end="url(#trail-mono)"/>

      <path class="trail" d="M480 360 V322 H462"/>
      <text class="trail-label" x="446" y="325.5" text-anchor="middle">$$$$</text>
      <path class="trail" d="M429 322 H412" marker-end="url(#trail-mono)"/>

      <text class="caption" x="349" y="440" text-anchor="middle">Traditionally, farmers sell their coffee for <tspan font-weight="700">1$ to $1.85 a pound</tspan></text>
    </g>

    <g class="direct">
      <rect class="figure" x="680" y="196" width="56" height="43" rx="6" role="img" aria-label="Coffee tree and farmer illustration"/>
      <text class="brand-label" x="713" y="252" text-anchor="middle">PRODUCER</text>
      <rect class="brand-mark" x="967" y="196" width="40" height="40"/>
      <text class="brand-label" x="987" y="252" text-anchor="middle">LARK HOLLOW</text>

      <text class="note" x="850" y="216" text-anchor="middle">We directly</text>
      <text class="note" x="850" y="231" text-anchor="middle">import &amp; roast</text>
      <text class="note" x="850" y="246" text-anchor="middle">the coffee</text>

      <path class="flow" d="M721 266 H979"/>
      <path class="flow" d="M845 363 L723 274" marker-end="url(#arrow-mono)"/>
      <path class="flow" d="M859 363 L979 274" marker-end="url(#arrow-mono)"/>

      <circle class="big-node" cx="713" cy="266" r="8"/><text class="big-num" x="713" y="270" text-anchor="middle">1</text>
      <circle class="big-node" cx="987" cy="266" r="8"/><text class="big-num" x="987" y="270" text-anchor="middle">2</text>
      <circle class="big-node" cx="850" cy="266" r="13"/>
      <ellipse class="bean" cx="850" cy="266" rx="6" ry="8.5" transform="rotate(25 850 266)"/>

      <text class="money" x="788" y="333" text-anchor="middle" transform="rotate(-35 788 326)">$$</text>
      <text class="money" x="920" y="333" text-anchor="middle" transform="rotate(35 920 326)">$$</text>

      <path class="icon" d="M831 332 H868 V345 A12 12 0 0 1 856 357 H843 A12 12 0 0 1 831 345 Z M868 336 H873 A6 6 0 0 1 873 348 H866"/>
      <rect class="brand-mark" x="843" y="337" width="13" height="13"/>
      <path class="icon" d="M845 325 Q842 320 845 316 M851 325 Q848 320 851 316" stroke-width="1.3"/>
      <circle class="node node--filled" cx="852" cy="370" r="8"/><text class="big-num big-num--light" x="852" y="374" text-anchor="middle">3</text>

      <text class="hero-coffee" x="853" y="398" text-anchor="middle">YOUR COFFEE</text>
      <text class="hero-sub" x="853" y="412" text-anchor="middle">FROM LARK HOLLOW</text>

      <text class="caption caption--wide" x="850" y="436" text-anchor="middle">We share revenues, guaranteeing our farmers <tspan font-weight="700">$3.25 a pound</tspan></text>
    </g>
  </svg>

</main>
</body>
</html>
```